Harborline Motors LLC

Car Dealer Customer Service
Address: 2741 Linden Avenue, Shelbyville, TN 37162
web: www.harborlinemotorstn.net
email: harborlinemotorstn@mailbox-example.net
Phone: (931) 555-0148
Phone: (629) 555-0173

```html
<!DOCTYPE html>
<html lang="en">
<head>
<meta charset="utf-8">
<title>Harborline Motors LLC – Business Card</title>
<link rel="stylesheet" href="https://fonts.googleapis.com/css2?family=Montserrat:wght@500;700;800;900&display=swap">
<style>
  :root {
    --backdrop: #e4e4e4;
    --yellow: #fbe12a;
    --amber: #f7b733;
    --orange: #f29a24;
    --blue: #1c6fae;
    --blue-light: #2f9bd6;
    --white: #ffffff;
  }
  * { margin: 0; padding: 0; box-sizing: border-box; }
  html, body {
    width: 1200px; height: 665px; overflow: hidden;
    background: var(--backdrop);
    font-family: "Montserrat", sans-serif;
  }
  .stage { position: relative; width: 1200px; height: 665px; }
  .card {
    position: absolute; top: 178px; width: 540px; height: 309px;
    overflow: hidden; box-shadow: 0 10px 30px rgba(0,0,0,.18);
  }
  .card--front {
    left: 40px;
    background: radial-gradient(circle at 48% 50%, var(--yellow) 0%, var(--amber) 75%, #f4ac3a 100%);
    display: flex; align-items: center; justify-content: center;
  }
  .brand { display: flex; align-items: center; gap: 10px; color: var(--blue); font-weight: 800; text-transform: uppercase; }
  .brand__dot { border-radius: 50%; background: var(--blue-light); flex: none; }
  .card--front .brand { font-size: 30px; }
  .card--front .brand__dot { width: 26px; height: 26px; }

  .card--back {
    left: 620px;
    background: radial-gradient(circle at 62% 45%, #fcd22c 0%, var(--amber) 55%, var(--orange) 100%);
  }
  .card--back .brand { position: absolute; left: 22px; top: 78px; font-size: 15px; gap: 7px; }
  .card--back .brand__dot { width: 14px; height: 14px; }
  .divider { position: absolute; inset: 0; }
  .car-photo {
    position: absolute; left: 140px; top: 112px; width: 250px; height: 150px;
    border-radius: 40% 40% 30% 30%;
    background: radial-gradient(ellipse at 50% 55%, #f5d21c 0%, #e8b81a 45%, rgba(60,60,60,.35) 80%, rgba(247,183,51,0) 100%);
  }
  .headline {
    position: absolute; right: 28px; top: 16px; text-align: right;
    font-weight: 900; font-size: 31px; line-height: .95; color: var(--white); text-transform: uppercase;
  }
  .headline__accent { color: var(--blue); }
  .call { position: absolute; left: 360px; top: 142px; color: var(--white); }
  .call__title { display: flex; align-items: center; gap: 8px; color: var(--blue); font-weight: 900; font-size: 22px; text-transform: uppercase; }
  .call__numbers { margin: 6px 0 0 36px; font-weight: 800; font-size: 15px; line-height: 1.3; }
  .contacts {
    position: absolute; left: 22px; right: 18px; bottom: 16px;
    display: flex; justify-content: space-between; align-items: flex-end;
    color: var(--white); font-weight: 500; font-size: 7.5px; text-transform: uppercase; letter-spacing: .2px;
  }
  .contact { display: flex; align-items: center; gap: 5px; line-height: 1.3; }
  .contact svg { flex: none; }
</style>
</head>
<body>
<main class="stage">
  <section class="card card--front" aria-label="Card front">
    <div class="brand"><span class="brand__dot"></span><span>Harborline Motors</span></div>
  </section>

  <section class="card card--back" aria-label="Card back">
    <div class="car-photo" role="img" aria-label="Photograph of a yellow sedan shown from the front three-quarter angle"></div>
    <svg class="divider" width="540" height="309" viewBox="0 0 540 309">
      <line x1="245" y1="40" x2="418" y2="285" stroke="#ffffff" stroke-width="2"/>
    </svg>
    <div class="brand"><span class="brand__dot"></span><span>Harborline Motors</span></div>
    <h1 class="headline">Car Dealer<br>Customer<br><span class="headline__accent">Service</span></h1>
    <div class="call">
      <div class="call__title">
        <svg width="28" height="28" viewBox="0 0 28 28" aria-hidden="true">
          <polygon points="14,1 25,7.5 25,20.5 14,27 3,20.5 3,7.5" fill="#1c6fae"/>
          <path d="M10 8c1 0 1.5 2.5 1 3.2l-1 .8c.8 2 2.2 3.4 4 4.2l.9-1c.8-.5 3.1 0 3.1 1.1v1.5c0 1-1 1.4-2 1.2-4.5-1-7.8-4.3-8.8-8.8C7 9.2 7.6 8 9 8z" fill="#ffffff"/>
        </svg>
        <span>Call Us</span>
      </div>
      <div class="call__numbers">(931) 555-0148<br>(629) 555-0173</div>
    </div>
    <address class="contacts" style="font-style:normal">
      <div class="contact">
        <svg width="8" height="11" viewBox="0 0 8 11" aria-hidden="true"><path d="M4 0a4 4 0 0 0-4 4c0 3 4 7 4 7s4-4 4-7a4 4 0 0 0-4-4zm0 5.5A1.5 1.5 0 1 1 4 2.5a1.5 1.5 0 0 1 0 3z" fill="#1c6fae"/></svg>
        <span>2741 Linden Avenue,<br>Shelbyville, TN 37162</span>
      </div>
      <div class="contact">
        <svg width="11" height="8" viewBox="0 0 11 8" aria-hidden="true"><rect width="11" height="8" rx="1" fill="#1c6fae"/><path d="M0.5 0.8 5.5 4.5 10.5 0.8" stroke="#ffffff" stroke-width="1" fill="none"/></svg>
        <span>harborlinemotorstn@mailbox-example.net</span>
      </div>
      <div class="contact">
        <svg width="10" height="10" viewBox="0 0 10 10" aria-hidden="true"><circle cx="5" cy="5" r="4.4" fill="none" stroke="#1c6fae" stroke-width="1.2"/><ellipse cx="5" cy="5" rx="1.8" ry="4.4" fill="none" stroke="#1c6fae" stroke-width="1"/><line x1="0.6" y1="5" x2="9.4" y2="5" stroke="#1c6fae" stroke-width="1"/></svg>
        <span>www.harborlinemotorstn.net</span>
      </div>
    </address>
  </section>
</main>
</body>
</html>
```